Financial & Tax Strategies

need to get a word press site with existing domains and condense existing content on existing site, make new site dynamic, need mobile too......need to take info from my brimlo website and get modern, relevant site, less verbose on first page, way more things to click and engage people. Would like it to look like this , but with my color scheme and not quite as busy looking. I like much of the content on my tabs. Want maximize by seo capabilities on their as well. The number one thing I can say is to go to my existing website and get content, logo, etc there … www.pineridgealdergroup.com .

Target Market(s)

Those 40 -65, business owners for at least 5 years. Higher net worth.

Number of Pages Required

5+ page

Font styles to use
Sans Serif

Colors
f04a50
e4daeb
ffffff

Requirements
Must have
• seo maximized, lots of places to click on to contact us, calls to action, relevant, conservative, want it to look like this and have the function as well.....slight variation on messaging, but like the simplicity on first view. https://www.dorvettalbrook.com/
Nice to have
• Some area along right side where videos we do will be.
Should not have
• feel too busy, but still have lots of opportunities to engage.

```html
<!DOCTYPE html>
<html lang="en">
<head>
<meta charset="utf-8">
<title>Pine Ridge Alder Group – Financial &amp; Tax Strategies</title>
<link href="https://fonts.googleapis.com/css2?family=Raleway:wght@300;400;500;600&display=swap" rel="stylesheet">
<style>
:root{
  --red:#f04a50;
  --lavender:#e4daeb;
  --white:#ffffff;
  --ink:#2a2a2e;
  --muted:#8c8a92;
  --line:#e6e3ea;
  --stage:#eeeef0;
  --footer:#2b2b30;
}
*{margin:0;padding:0;box-sizing:border-box}
html,body{width:800px;height:1200px;overflow:hidden;background:var(--stage);font-family:'Raleway',sans-serif;color:var(--ink)}
h1,h2,h3{font-weight:400}
.page{position:absolute;left:242px;top:0;width:380px;height:1442px;background:var(--white);transform:scale(0.832);transform-origin:0 0;box-shadow:4px 4px 10px rgba(0,0,0,.25)}
.abs{position:absolute}
.site-header{position:absolute;left:0;width:380px;height:18px;display:flex;align-items:center;padding:0 38px}
.site-header.sticky{top:182px;background:var(--white);border-bottom:1px solid var(--line)}
.site-header.hero-top{top:0}
.brand{font-size:5px;line-height:5.4px;font-weight:500;color:var(--ink);font-family:'Raleway',sans-serif}
.nav{margin-left:auto;display:flex;align-items:center;gap:6px;font-size:3.4px;color:var(--muted)}
.nav .active{color:var(--red)}
.nav .pill{border:0.6px solid var(--red);color:var(--red);border-radius:4px;padding:1px 3px}
.nav .dot{width:2.4px;height:2.4px;border-radius:50%;background:var(--muted)}
.hero{position:absolute;left:0;top:0;width:380px;height:182px;background:linear-gradient(180deg,#fbeaec 0%,#f6c2c6 55%,#f2a3a9 100%)}
.hero-eyebrow{top:69px;left:0;width:380px;text-align:center;font-size:4.4px;letter-spacing:1.2px;font-weight:600}
.hero-title{top:80px;left:72px;display:flex;align-items:center;font-size:18px;font-weight:400;letter-spacing:.3px}
.hero-title .grow{background:var(--red);color:var(--white);padding:1px 4px;margin-right:4px;letter-spacing:1.5px}
.hero-link{top:127px;left:0;width:380px;text-align:center;font-size:4px;color:var(--white);font-weight:600;letter-spacing:.5px}
.hero-link span{border-bottom:0.6px solid var(--white);padding-bottom:1px}
.eyebrow{font-size:3.4px;letter-spacing:1px;font-weight:600;color:var(--muted);text-transform:uppercase}
.section-title{font-size:11px;font-weight:400}
.section-title em{font-style:normal;color:var(--red)}
.centered{left:0;width:380px;text-align:center}
.about-label{top:234px;left:66px}
.about-mark{top:251px;left:116px;width:50px;height:50px;border-radius:50%;background:var(--lavender);opacity:.8}
.about-title{top:246px;left:66px;font-size:11px;line-height:15.5px;font-weight:400}
.about-title .red{color:var(--red)}
.about-and{top:262px;left:118px;font-size:10px;font-weight:400}
.copy{font-size:3.6px;line-height:7.4px;color:var(--muted)}
.about-copy{top:232px;left:192px;width:120px}
.intro-copy{top:381px;left:62px;width:252px}
.intro-copy p+p{margin-top:5px}
.intro-copy b{color:var(--ink);font-weight:600}
.finance-art{top:440px;left:0;width:380px;height:120px;background:radial-gradient(ellipse at 55% 70%,#d9cce4 0%,#ebe3f0 45%,rgba(255,255,255,0) 75%)}
.finance-art-core{top:448px;left:52px;width:276px;height:95px;border-radius:40px 40px 6px 6px;background:linear-gradient(180deg,#efe8f3,#dccfe6)}
.text-link{font-size:3.6px;font-weight:600;letter-spacing:.4px}
.text-link span{border-bottom:0.6px solid var(--ink);padding-bottom:1px}
.contact-now{top:463px;left:267px}
.services-label{top:577px}
.services-title{top:587px}
.service-card{top:612px;width:95px;height:70px;background:var(--white);box-shadow:0 1px 4px rgba(0,0,0,.12);overflow:hidden}
.service-card h3{position:absolute;top:22px;left:9px;font-size:3.8px;font-weight:500}
.service-card.featured{background:linear-gradient(180deg,#f26a70,var(--red))}
.service-card.featured h3{color:var(--white)}
.service-card svg{position:absolute;left:0;bottom:0}
.card-more{position:absolute;left:9px;bottom:6px;font-size:3px;color:var(--white)}
.services-note{top:697px;left:90px;width:200px;text-align:center}
.call-line{top:726px;font-size:10px;font-weight:400}
.call-line em{font-style:normal;color:var(--red)}
.team-label{top:785px}
.team-title{top:795px}
.team-photo{top:820px;width:94px;height:127px;background:linear-gradient(180deg,#f4f4f4,#d8d8d8)}
.radio-copy{top:990px;left:40px;width:148px;font-size:5.4px;line-height:7.4px}
.radio-sub{top:1020px;left:40px;width:148px;font-size:3.6px;color:var(--muted)}
.radio-badge{top:1038px;left:88px;width:50px;height:14px;background:#d21f8a;border-radius:1px}
.office-photo{top:972px;left:191px;width:147px;height:98px;background:linear-gradient(90deg,#d64a4e 0%,#e9e3dc 38%,#f3f1ee 70%,#d9c7b0 100%)}
.clients-label{top:1112px}
.clients-title{top:1122px}
.client-grid{top:1150px;left:40px;width:300px;height:86px;display:grid;grid-template-columns:repeat(4,1fr);grid-template-rows:repeat(2,1fr)}
.client-cell{display:flex;align-items:center;justify-content:center;border-right:1px solid var(--line);border-bottom:1px solid var(--line)}
.client-cell:nth-child(4n){border-right:none}
.client-cell:nth-child(n+5){border-bottom:none}
.client-badge{width:38px;height:10px;background:#cfcfd4;border-radius:2px}
.client-badge.round{width:26px;height:14px;border-radius:50%}
.callback{top:1265px;left:0;width:380px;height:167px;background:var(--red);color:var(--white)}
.callback-title{top:37px;left:37px;font-size:11px;line-height:15px;font-weight:400}
.callback-rule{top:80px;left:37px;width:24px;height:1px;background:var(--white)}
.callback-note{top:106px;left:37px;width:92px;font-size:3.4px;line-height:5.4px;color:#ffe3e4}
.field{left:142px;width:198px;height:9px;border:0.6px solid rgba(255,255,255,.6);font-size:3px;color:#ffe3e4;padding:2px 3px}
.field.message{height:37px}
.send-btn{top:119px;left:142px;width:62px;height:13px;background:var(--white);color:var(--ink);font-size:3.4px;font-weight:600;letter-spacing:.4px;display:flex;align-items:center;justify-content:center}
.site-footer{top:1432px;left:0;width:380px;height:10px;background:var(--footer);color:#9c9aa3;font-size:2.8px;display:flex;align-items:center;justify-content:center}
</style>
</head>
<body>
<div class="page">

  <section class="hero" role="img" aria-label="Soft red-tinted photo of a business owner working at a desk"></section>
  <header class="site-header hero-top">
    <div class="brand">Pine Ridge<br>Alder Group</div>
    <nav class="nav"><span class="active">Home</span><span>About Us</span><span>Our Services</span><span class="pill">Contact Us</span><span class="dot"></span><span class="dot"></span><span class="dot"></span></nav>
  </header>
  <div class="abs hero-eyebrow">HELPING YOU TO</div>
  <h1 class="abs hero-title"><span class="grow">GROW</span>YOUR BUSINESS</h1>
  <div class="abs hero-link"><span>QUICK CALL BACK</span></div>

  <header class="site-header sticky">
    <div class="brand">Pine Ridge<br>Alder Group</div>
    <nav class="nav"><span class="active">Home</span><span>About Us</span><span>Our Services</span><span class="pill">Contact Us</span><span class="dot"></span><span class="dot"></span><span class="dot"></span></nav>
  </header>

  <div class="abs eyebrow about-label">About us</div>
  <div class="abs about-mark"></div>
  <h2 class="abs about-title">Solid<br><span class="red">Solu</span><br>Achievement</h2>
  <div class="abs about-and">&amp; Perfect</div>
  <p class="abs copy about-copy">When the market is up, all advisors are brilliant. It is when the market corrects that steady planning matters most. For decades our team has helped owners protect what they built and prepare for what comes next. We believe good advice should be clear, patient and personal. Our planners listen first, explain every option in plain terms and stay with you through every season of the market. We look at taxes, income, risk and family goals together, so nothing is planned in isolation. Our strategies are the same ones we use for our own households, and we are always available to talk them through with you.</p>

  <div class="abs copy intro-copy">
    <p><b>Pine Ridge Alder Group</b> does not chase fads. We build lasting plans around your income, your taxes and your family so that each decision supports the next. Whether you are growing a company or preparing to step away, we help you keep more of what you earn.</p>
    <p>Many advisors sell products. We prefer to start with a conversation about your goals, your timeline and the legacy you want to leave behind.</p>
  </div>

  <div class="abs finance-art"></div>
  <div class="abs finance-art-core" role="img" aria-label="Illustration of hands holding coins above a bank, briefcase, charts and calculator"></div>
  <div class="abs text-link contact-now"><span>CONTACT US NOW</span></div>

  <div class="abs eyebrow centered services-label">Services</div>
  <h2 class="abs section-title centered services-title">Our <em>Services</em></h2>

  <article class="abs service-card featured" style="left:40px">
    <h3>Investments Management</h3>
    <svg width="95" height="40" viewBox="0 0 95 40"><polygon points="0,40 0,26 18,14 30,22 46,8 62,20 76,12 95,24 95,40" fill="#ffffff" fill-opacity=".22"/><polygon points="0,40 0,32 22,22 40,30 58,18 78,28 95,22 95,40" fill="#ffffff" fill-opacity=".18"/></svg>
    <span class="card-more">Learn more</span>
  </article>
  <article class="abs service-card" style="left:142px">
    <h3>Financial Planning</h3>
    <svg width="95" height="45" viewBox="0 0 95 45"><rect x="40" y="20" width="8" height="20" fill="#f04a50"/><rect x="52" y="10" width="8" height="30" fill="#f04a50"/><rect x="28" y="28" width="8" height="12" fill="#f6a1a4"/><text x="66" y="28" font-family="Raleway,sans-serif" font-size="10" fill="#f04a50">%</text><line x1="8" y1="40" x2="88" y2="40" stroke="#e6e3ea" stroke-width="0.8"/></svg>
  </article>
  <article class="abs service-card" style="left:243px">
    <h3>Taxes Planning</h3>
    <svg width="95" height="45" viewBox="0 0 95 45"><path d="M0 38 C20 36 32 22 46 26 S72 8 95 4 L95 45 L0 45Z" fill="#fbd6d8"/><path d="M0 38 C20 36 32 22 46 26 S72 8 95 4" fill="none" stroke="#f04a50" stroke-width="1"/><circle cx="46" cy="26" r="1.6" fill="#f04a50"/><circle cx="80" cy="8" r="1.6" fill="#f04a50"/></svg>
  </article>

  <p class="abs copy services-note">Your plan should reflect your goals, not a sales quota. We review every account with care and report results in plain language.</p>
  <p class="abs centered call-line">Give us a call at <em>916.555.0142</em></p>

  <div class="abs eyebrow centered team-label">Meet our team</div>
  <h2 class="abs section-title centered team-title">Company more <em>like a family</em></h2>
  <div class="abs team-photo" style="left:40px" role="img" aria-label="Black and white portrait of a smiling team member"></div>
  <div class="abs team-photo" style="left:142px" role="img" aria-label="Black and white portrait of a team member in a white shirt"></div>
  <div class="abs team-photo" style="left:243px" role="img" aria-label="Black and white portrait of a team member with crossed arms"></div>

  <p class="abs radio-copy">Catch Pine Ridge Alder Group's fun &amp; revealing Cash Carl &amp; Everyday Ed Saturdays &amp; Sundays at 6 am on Crestwave Radio's weekend talk hour.</p>
  <p class="abs radio-sub">You can also catch our past shows by clicking on the link below.</p>
  <div class="abs radio-badge"></div>
  <div class="abs office-photo" role="img" aria-label="Bright office reception with a red wall, plant and front desk"></div>

  <div class="abs eyebrow centered clients-label">Clients and partners</div>
  <h2 class="abs section-title centered clients-title">Satisfied customers</h2>
  <div class="abs client-grid">
    <div class="client-cell"><span class="client-badge"></span></div>
    <div class="client-cell"><span class="client-badge"></span></div>
    <div class="client-cell"><span class="client-badge round"></span></div>
    <div class="client-cell"><span class="client-badge"></span></div>
    <div class="client-cell"><span class="client-badge round"></span></div>
    <div class="client-cell"><span class="client-badge round"></span></div>
    <div class="client-cell"><span class="client-badge"></span></div>
    <div class="client-cell"><span class="client-badge round"></span></div>
  </div>

  <section class="abs callback">
    <h2 class="abs callback-title">Request<br>a call back</h2>
    <div class="abs callback-rule"></div>
    <p class="abs callback-note">We will answer within one business day with times that suit you.</p>
    <div class="abs field" style="top:30px">Your Name *</div>
    <div class="abs field" style="top:45px">Your Email *</div>
    <div class="abs field" style="top:60px">Subject</div>
    <div class="abs field message" style="top:76px">Your Message</div>
    <div class="abs send-btn">SEND MESSAGE</div>
  </section>

  <footer class="abs site-footer">Copyright 2024 Pine Ridge Alder Group. All rights reserved.</footer>
</div>
</body>
</html>
```